American alt-rock band needs eye-catching album cover for new record

We need an album cover for our new cd. The band is called Velvet Lantern, the music is alt-rock, an interesting mix of styles and infuences- Elements of The Hollows, Q9, Dan Harlow, Carl Berry The Pilots and Marvin Olendorf are all evident in the sound. Classic rock with atmospheric elements and sweeping melodies. The album is titled "Nothing Stays Where You Left It". We are interested in designs that focus on a single direct subject and are not too busy in nature. Visually striking, yet simple and memorable. Stark contrasts between dark and light. Album covers such as Glasshouse Unit's "Trespass", Amber Tide's "Quiet Edge of The Tide" and Iron Lark's self titled release are along the lines of what we were hoping for. An idea we had included an image of a man looking at two doors, or two paths, something involving the imagery of decisions (a door number one or number two type concept). Also like simple designs maybe with the subject in a lower corner of the image (this doesn't have to followed if it makes more sense for the image to be centered though). Solid color backgrounds. Colors we like include black, white,deep reds/blues/purples. Not all of them need to be included, but could be (white/black, white/purple, black/red, etc) Please include the band name and album name within the design.

Target Market(s)

18-39

Colors
6b449b
ec1f27
000000
474747
fbfbfb

Requirements
Must have
• Band name and album title must be included in design
Nice to have
• Would like to see something "dream-like" but not too much outer space/sci-fi imagery. Would like to see the moon motel image that I have added used in some way.
Should not have
• no skulls or heavy metal imagery. Dark is ok, but in a more artistic way.

```html
<!DOCTYPE html>
<html lang="en">
<head>
<meta charset="utf-8">
<title>Nothing Stays Where You Left It — Velvet Lantern</title>
<link rel="stylesheet" href="https://fonts.googleapis.com/css2?family=Arimo:wght@700&display=swap">
<style>
  :root {
    --ink-black: #000000;
    --deep-magenta: #8a0f86;
    --hot-magenta: #e21ee0;
    --glow-pink: #f6a8f4;
    --core-white: #fffaff;
    --text-white: #fbfbfb;
    --cover-size: 1200px;
  }

  html, body {
    margin: 0;
    padding: 0;
    width: var(--cover-size);
    height: var(--cover-size);
    overflow: hidden;
    background: var(--ink-black);
  }

  .album-cover {
    position: relative;
    width: var(--cover-size);
    height: var(--cover-size);
    overflow: hidden;
    background: var(--ink-black);
    font-family: "Arimo", Arial, sans-serif;
  }

  .cover-artwork {
    position: absolute;
    inset: 0;
    background:
      radial-gradient(circle at 49% 24%,
        var(--core-white) 0%,
        var(--glow-pink) 6%,
        var(--hot-magenta) 20%,
        var(--deep-magenta) 48%,
        rgba(40, 0, 40, 0.9) 72%,
        var(--ink-black) 92%),
      linear-gradient(to bottom,
        transparent 55%,
        rgba(150, 10, 140, 0.55) 70%,
        var(--ink-black) 100%);
    background-blend-mode: screen;
  }

  .cover-titles {
    position: absolute;
    left: 0;
    right: 0;
    top: 1000px;
    text-align: center;
    color: var(--text-white);
  }

  .album-title {
    margin: 0;
    font-size: 53px;
    font-weight: 700;
    letter-spacing: 0.07em;
    word-spacing: 0.12em;
    line-height: 1.2;
  }

  .band-name {
    margin: 30px 0 0;
    font-size: 33px;
    font-weight: 700;
    letter-spacing: 0.07em;
    word-spacing: 0.1em;
    line-height: 1.2;
  }
</style>
</head>
<body>
  <main class="album-cover">
    <div class="cover-artwork" role="img" aria-label="Dreamlike space scene: a brilliant white star flaring inside a magenta halo, a small ringed planet at upper left, and a magenta halftone dot field fading into black"></div>
    <div class="cover-titles">
      <h1 class="album-title">Nothing Stays Where You Left It</h1>
      <p class="band-name">Velvet Lantern</p>
    </div>
  </main>
</body>
</html>
```